LOGO DESIGN: Construction Related Service Business

We require a logo for our business Dovtar Services. We are a construction related business offering a range of services including machine services for groundworks (digging trenches, soak wells, preparing land for construction etc), demolition and truck haulage from demolition sites.
We would like our logo to be predominately text, but may include abstract graphics. The colour scheme should be mainly a mid bright blue and overall be quite 'clean'.

Industry/Entity Type

Construction

Contact Information for Business Card

Colin Pruett
Ph:041 562 9083
dovtarservices@keloran.com.au

Colors
0456a3

```html
<!DOCTYPE html>
<html lang="en">
<head>
<meta charset="utf-8">
<title>Dovtar Services – Business Card</title>
<link rel="stylesheet" href="https://fonts.googleapis.com/css2?family=Crimson+Text:wght@400&display=swap">
<style>
  :root {
    --card-blue: #0a3fdc;
    --card-blue-light: #0b4ff5;
    --card-blue-deep: #0232c8;
    --card-text: #ffffff;
  }
  html, body {
    margin: 0;
    padding: 0;
    width: 1200px;
    height: 741px;
    overflow: hidden;
    background: var(--card-blue);
  }
  .business-card {
    display: block;
    width: 1200px;
    height: 741px;
  }
  .card-text {
    font-family: "Crimson Text", "Minion Pro", Georgia, serif;
    fill: var(--card-text);
  }
  .company-name {
    font-size: 164px;
  }
  .contact-line {
    font-size: 58px;
  }
</style>
</head>
<body>
  <svg class="business-card" viewBox="0 0 1200 741" xmlns="http://www.w3.org/2000/svg">
    <defs>
      <radialGradient id="gear-field-tone" cx="45%" cy="40%" r="75%">
        <stop offset="0%" stop-color="var(--card-blue-light)"/>
        <stop offset="55%" stop-color="var(--card-blue)"/>
        <stop offset="100%" stop-color="var(--card-blue-deep)"/>
      </radialGradient>
    </defs>

    <rect class="gear-pattern-backdrop" x="0" y="0" width="1200" height="741"
          fill="url(#gear-field-tone)" role="img"
          aria-label="Background pattern of overlapping blue gears"/>

    <text class="card-text company-name" x="94" y="216">Dovtar Services</text>

    <g class="contact-details">
      <text class="card-text contact-line" x="94" y="472">Colin Pruett</text>
      <text class="card-text contact-line" x="94" y="548">Phone: 041 562 9083</text>
      <text class="card-text contact-line" x="94" y="624">Email: dovtarservices@keloran.com.au</text>
    </g>
  </svg>
</body>
</html>
```